Established food business needs a new name card design

Refer to attached current name card. Would like a new professional look design with only the company name and logo without any pictures. Would like green and yellow to be included.
To include:
My name "HAKIM RUSLAN" and hand phone number "86207319".
To delete "
"Along Pinegrove Ave 3" and
"www.bu-tirah.com.sg"
To change email to:
"rvk27@tealmail.com.sg"

```html
<!DOCTYPE html>
<html lang="en">
<head>
<meta charset="utf-8">
<title>Bu-Tirah Eating Corner – Name Card</title>
<link rel="stylesheet" href="https://fonts.googleapis.com/css2?family=Montserrat:wght@300;400;500;600&display=swap">
<style>
  :root {
    --stage: #1a1a1a;
    --stage-light: #2e2e2e;
    --yellow: #f2cb05;
    --green: #0f4a2c;
    --green-deep: #0c3b23;
    --paper: #f6f6f4;
    --tagline: #9c9a86;
    --tagline-front: #c9c39f;
  }
  * { box-sizing: border-box; margin: 0; padding: 0; }
  html, body { width: 1200px; height: 900px; overflow: hidden; }
  body {
    background: radial-gradient(ellipse at 50% 35%, var(--stage-light), var(--stage) 70%);
    font-family: "Montserrat", sans-serif;
    position: relative;
  }
  .card {
    position: absolute;
    left: 290px;
    width: 620px;
    height: 354px;
    overflow: hidden;
    box-shadow: 0 14px 30px rgba(0,0,0,.55);
  }
  .card--front { top: 60px; background: var(--green-deep); }
  .card--back  { top: 480px; background: var(--paper); }

  .brand {
    position: absolute;
    display: flex; flex-direction: column; align-items: flex-start;
  }
  .brand__row { display: flex; align-items: center; gap: 14px; }
  .brand__dot {
    width: 56px; height: 56px; border-radius: 50%;
    border: 4px solid var(--yellow);
    flex: none;
  }
  .brand__name {
    color: var(--yellow);
    font-weight: 600;
    font-size: 40px;
    letter-spacing: 1px;
    line-height: 1;
    white-space: nowrap;
  }
  .brand__tagline {
    margin-left: 70px;
    margin-top: 8px;
    font-weight: 300;
    font-size: 11px;
    letter-spacing: 6px;
    color: var(--tagline);
    border-top: 1px solid rgba(156,154,134,.5);
    padding-top: 5px;
    white-space: nowrap;
  }
  .card--front .brand { left: 150px; top: 130px; }
  .card--front .brand__tagline { color: var(--tagline-front); border-top-color: rgba(201,195,159,.5); }
  .card--back .brand { left: 36px; top: 138px; }
  .card--back .brand__name { font-size: 36px; }

  .divider {
    position: absolute; left: 330px; top: 118px;
    width: 2px; height: 120px; background: var(--green);
  }
  .contact { position: absolute; left: 354px; top: 118px; }
  .contact__name {
    color: var(--yellow); font-weight: 500; font-size: 24px; letter-spacing: 1px;
    white-space: nowrap; line-height: 1.2;
  }
  .contact__role { color: var(--green); font-size: 16px; margin-top: 2px; }
  .contact__list { list-style: none; margin-top: 20px; }
  .contact__item {
    display: flex; align-items: center; gap: 10px;
    color: var(--green); font-size: 16px; line-height: 27px;
    white-space: nowrap;
  }
  .contact__item svg { width: 13px; height: 13px; flex: none; fill: none; stroke: var(--yellow); stroke-width: 2; }
</style>
</head>
<body>
  <section class="card card--front">
    <div class="brand">
      <div class="brand__row">
        <span class="brand__dot"></span>
        <span class="brand__name">BU-TIRAH</span>
      </div>
      <span class="brand__tagline">EATING CORNER</span>
    </div>
  </section>

  <section class="card card--back">
    <div class="brand">
      <div class="brand__row">
        <span class="brand__dot"></span>
        <span class="brand__name">BU-TIRAH</span>
      </div>
      <span class="brand__tagline">EATING CORNER</span>
    </div>
    <div class="divider"></div>
    <div class="contact">
      <p class="contact__name">HAKIM RUSLAN</p>
      <p class="contact__role">Director</p>
      <ul class="contact__list">
        <li class="contact__item">
          <svg viewBox="0 0 16 16"><path d="M4 1.5 L6.5 4.5 L5 6.5 Q6.5 9.5 9.5 11 L11.5 9.5 L14.5 12 L12.5 14.5 Q4 13 1.5 3.5 Z"/></svg>
          86207319
        </li>
        <li class="contact__item">
          <svg viewBox="0 0 16 16"><rect x="1.5" y="3.5" width="13" height="9"/><path d="M1.5 3.5 L8 9 L14.5 3.5"/></svg>
          rvk27@tealmail.com.sg
        </li>
      </ul>
    </div>
  </section>
</body>
</html>
```